Need Eye Catching For Sale By Owner Signs

In need of a Eye Catching For Sale By Owner Sign design. I plan on using the sign to market buildings and raw land that I own. The design should be able to scale to different rectangular dimensions for example a yard stake sign or a large 4' x 6' sign to be tacked to plywood. The design should have a dead space near the bottom that I can insert more detail information into at a later time.

The main tag line "For Sale By Owner" and the contact number "319-562-4097" needs to be easily be read from a distance.

```html
<!DOCTYPE html>
<html lang="en">
<head>
<meta charset="utf-8">
<title>For Sale By Owner Sign</title>
<link rel="stylesheet" href="https://fonts.googleapis.com/css2?family=Archivo+Black&family=Pacifico&display=swap">
<style>
  :root {
    --brown: #7b4a31;
    --taupe: #9e8679;
    --white: #ffffff;
  }
  html, body {
    margin: 0;
    padding: 0;
    width: 1200px;
    height: 816px;
    overflow: hidden;
    background: var(--white);
  }
  .sign {
    position: relative;
    width: 1200px;
    height: 816px;
    background: var(--white);
  }
  .sign-art {
    position: absolute;
    inset: 0;
  }
  .headline, .subline, .phone {
    font-family: "Archivo Black", "Arial Black", sans-serif;
  }
  .call-label {
    font-family: "Pacifico", cursive;
  }
  .landscape {
    position: absolute;
    left: 58px;
    top: 565px;
    width: 306px;
    height: 192px;
    background: radial-gradient(ellipse at 55% 40%, var(--brown) 0%, rgba(123, 74, 49, 0.85) 45%, rgba(123, 74, 49, 0) 72%);
  }
</style>
</head>
<body>
  <main class="sign">
    <svg class="sign-art" width="1200" height="816" viewBox="0 0 1200 816">
      <rect class="top-band" x="0" y="0" width="1200" height="278" fill="var(--brown)"/>
      <rect class="owner-band" x="0" y="278" width="1200" height="134" fill="var(--taupe)"/>
      <polyline class="frame" points="52,412 52,36 1150,36 1150,412" fill="none" stroke="var(--white)" stroke-width="3"/>
      <text class="headline" x="77" y="240" font-size="250" fill="var(--white)" textLength="997" lengthAdjust="spacingAndGlyphs">FOR SALE</text>
      <text class="call-label" x="77" y="393" font-size="46" fill="var(--white)">Call</text>
      <text class="subline" x="249" y="389" font-size="136" fill="var(--white)" textLength="757" lengthAdjust="spacingAndGlyphs">BY OWNER</text>
      <text class="phone" x="115" y="533" font-size="142" fill="var(--brown)" textLength="978" lengthAdjust="spacingAndGlyphs">319-562-4097</text>
    </svg>
    <div class="landscape" role="img" aria-label="Illustration of two leafy trees on a gently rolling hill"></div>
  </main>
</body>
</html>
```